Electronic Refurbishment Warehouse needs a Website

We are looking for a clean, professional looking design with iconic imagery. Our main point we want to get across is that we will help clients save time, and money, and provide outstanding quality. Our logo can be found in the uploads section. This site is used to impress clients that we have a pre-existing relationship with. This site will be available for the public but it will not be used to advertise to the public or to drive traffic to it. The color scheme we are looking to stay with is blue, but that is not to say that everything should be a shade of blue. Last note, see site map below.

Site Map:

Home
Company
a. company overview
b. CEO letter
Services
a. Remanufacture & Refurbishment Services
1. Consumer Electronics
2. Cellular Phones
b.Reverse Logistics Management
c.Warranty Repair & Field Services
d.Quality Control & Assurance
e.Warehousing & Distribution
Careers
Contact Us
Updates

Project Deadline Extended
Reason: We want to allocate more time for designers to do what they do best.

Target Market(s)

Phone and TV Retailers that may have units that need to be refurbished. Example Vorelli, tradequay, qlm, etc.

Industry/Entity Type

Electronics

Requirements
Must have
• Home Page Slider.
Iconic imagery and navigation.
The ability to be put into the 960 Grid.

```html
<!DOCTYPE html>
<html lang="en">
<head>
<meta charset="utf-8">
<title>Norvane Group – Remanufacture &amp; Refurbishment</title>
<link rel="stylesheet" href="https://fonts.googleapis.com/css2?family=Arimo:wght@400;700&display=swap">
<style>
  :root {
    --ink: #222;
    --body-text: #555;
    --nav-text: #555;
    --brand-blue: #2a6db5;
    --rule: #c8c8c8;
    --frame: #bdbdbd;
    --green: #3a9a0e;
    --green-dark: #2c7d07;
    --link-green: #3a9a0e;
    --header-top: #ffffff;
    --header-bottom: #f2f0e6;
    --footer-bg: #404040;
    --footer-text: #ffffff;
    --page-bg: #ffffff;
  }
  * { box-sizing: border-box; margin: 0; padding: 0; }
  html, body { width: 1200px; height: 1011px; overflow: hidden; background: var(--page-bg); }
  body { position: relative; font-family: "Arimo", Arial, sans-serif; color: var(--ink); }

  .site-header {
    position: absolute; left: 0; top: 0; width: 1200px; height: 95px;
    background: linear-gradient(var(--header-top), var(--header-bottom));
    border-bottom: 1px solid #8e8e8e;
  }
  .brand {
    position: absolute; left: 145px; top: 30px;
    display: flex; align-items: center; gap: 10px;
    font-size: 27px; font-weight: 700; color: var(--brand-blue);
  }
  .brand-mark { width: 30px; height: 30px; background: var(--brand-blue); }
  .search {
    position: absolute; left: 877px; top: 18px; width: 178px; height: 28px;
    border: 1px solid #9a9a9a; border-radius: 14px; background: #fff;
    font-size: 16px; color: #555; padding: 5px 0 0 11px;
  }
  .search svg { position: absolute; right: 8px; top: 3px; }
  .main-nav { position: absolute; top: 59px; left: 0; width: 1200px; font-size: 16.5px; color: var(--nav-text); }
  .main-nav span { position: absolute; white-space: nowrap; }

  .hero {
    position: absolute; left: 142px; top: 116px; width: 916px; height: 349px;
    border: 1px solid var(--frame);
  }
  .hero-photo {
    position: absolute; left: 28px; top: 36px; width: 451px; height: 305px;
    background: linear-gradient(180deg, #d9dcdf 0%, #eef0f2 60%, #ffffff 100%);
  }
  .hero-title {
    position: absolute; left: 545px; top: 22px; width: 340px; text-align: center;
    font-size: 26px; line-height: 31px; color: var(--brand-blue);
  }
  .hero-text {
    position: absolute; left: 568px; top: 138px; width: 286px;
    font-size: 15px; line-height: 20px; color: var(--body-text); text-align: justify;
  }
  .btn-read {
    position: absolute; left: 738px; top: 273px; width: 117px; height: 32px;
    border-radius: 3px; background: linear-gradient(var(--green), var(--green-dark));
    color: #fff; font-size: 16.5px; text-align: center; line-height: 32px;
  }

  .service { position: absolute; top: 484px; width: 166px; text-align: center; }
  .service-photo { width: 166px; height: 130px; border: 1px solid var(--frame); }
  .service-label { margin-top: 9px; font-size: 16.5px; line-height: 18px; color: #111; }

  .welcome { position: absolute; left: 143px; top: 692px; width: 633px; }
  .section-title { font-size: 22px; font-weight: 400; color: var(--ink); margin-bottom: 8px; }
  .welcome p { font-size: 14px; line-height: 17px; color: var(--body-text); text-align: justify; margin-bottom: 17px; }
  .divider { position: absolute; left: 786px; top: 709px; height: 223px; border-left: 1px dotted #777; }

  .news { position: absolute; left: 799px; top: 692px; width: 259px; }
  .news-item { padding-bottom: 10px; border-bottom: 1px dotted #777; margin-bottom: 14px; }
  .news-item:last-child { border-bottom: 0; }
  .news-date { font-size: 14px; font-weight: 700; color: #111; margin-bottom: 1px; }
  .news-item p { font-size: 14px; line-height: 17px; color: var(--body-text); text-align: justify; }
  .news-more { display: block; text-align: right; font-size: 14px; color: var(--link-green); margin-top: 5px; }

  .site-footer {
    position: absolute; left: 0; top: 953px; width: 1200px; height: 58px;
    background: var(--footer-bg); color: var(--footer-text); font-size: 14px;
  }
  .footer-nav { position: absolute; left: 145px; top: 14px; }
  .footer-legal { position: absolute; right: 119px; top: 11px; text-align: right; line-height: 18px; }
</style>
</head>
<body>
  <header class="site-header">
    <div class="brand"><span class="brand-mark"></span>Norvane group</div>
    <div class="search">Search
      <svg width="24" height="22" viewBox="0 0 24 22"><circle cx="9" cy="9" r="6" fill="none" stroke="#555" stroke-width="2.5"/><line x1="13.5" y1="13.5" x2="20" y2="19" stroke="#555" stroke-width="3" stroke-linecap="round"/></svg>
    </div>
    <nav class="main-nav">
      <span style="left:597px">Home</span>
      <span style="left:676px">Company</span>
      <span style="left:783px">Services</span>
      <span style="left:882px">Careers</span>
      <span style="left:977px">Contact Us</span>
    </nav>
  </header>

  <section class="hero">
    <div class="hero-photo" role="img" aria-label="Photo of a refurbished slide-out keyboard smartphone shown from front, open and side"></div>
    <h1 class="hero-title" style="font-weight:400">Remanufacture<br>&amp;<br>Refurbishment Services</h1>
    <p class="hero-text">Lorem ipsum dolor sit amet, consecte-tur adipiscing elit. Morbi congue quam vitae lacus vestibulum auctor. Pha-sellus vel mauris quis nibh scelerisque dignissim sed at libero.</p>
    <a class="btn-read">Read More</a>
  </section>

  <div class="service" style="left:142px">
    <div class="service-photo" role="img" aria-label="Flat-screen television with a media player" style="background:linear-gradient(#ffffff,#d6d8da)"></div>
    <div class="service-label">Consumer Electronics</div>
  </div>
  <div class="service" style="left:329px">
    <div class="service-photo" role="img" aria-label="Group of smartphones" style="background:linear-gradient(#e8ebee,#9aa2aa)"></div>
    <div class="service-label">Cellular Phones</div>
  </div>
  <div class="service" style="left:517px">
    <div class="service-photo" role="img" aria-label="Smartphone with wrench and screwdriver" style="background:linear-gradient(#ffffff,#cfd8e2)"></div>
    <div class="service-label">Warranty Repair &amp;<br>Field Services</div>
  </div>
  <div class="service" style="left:704px">
    <div class="service-photo" role="img" aria-label="Quality approved stamp" style="background:radial-gradient(circle,#e5f3e5 0%,#ffffff 70%)"></div>
    <div class="service-label">Quality Control &amp;<br>Assurance</div>
  </div>
  <div class="service" style="left:892px">
    <div class="service-photo" role="img" aria-label="Warehouse racking loaded with boxes" style="background:linear-gradient(#f0e6e6,#c99393)"></div>
    <div class="service-label">Warehousing &amp;<br>Distribution</div>
  </div>

  <section class="welcome">
    <h2 class="section-title">Welcome to Norvane Group</h2>
    <p>Lorem ipsum dolor sit amet, consectetur adipiscing elit. Morbi congue quam vitae lacus vestibulum auctor. Phasellus vel mauris quis nibh scelerisque dignissim sed at libero. Pellentesque habitant morbi tristique senectus et netus et malesuada fames ac turpis egestas. Aenean a dapibus libero. Praesent non orci fermentum arcu rutrum pharetra. In iaculis, dolor et consectetur pretium, nulla magna elementum nisi, quis mattis diam metus eget lacus. Mauris et elit nibh. Praesent elementum, urna ac volutpat accumsan, est dolor venenatis ligula, vel sodales dolor urna quis justo. Pellentesque viverra, augue id auctor imperdiet, quam tellus venenatis eros, non tristique urna diam sed eros.</p>
    <p>Lorem ipsum dolor sit amet, consectetur adipiscing elit. Morbi congue quam vitae lacus vestibulum auctor. Phasellus vel mauris quis nibh scelerisque dignissim sed at libero. Pellentesque habitant morbi tristique senectus et netus et malesuada fames ac turpis egestas. Aenean a dapibus libero. Praesent non orci fermentum arcu rutrum pharetra.</p>
  </section>
  <div class="divider"></div>

  <aside class="news">
    <h2 class="section-title">Latest News</h2>
    <article class="news-item">
      <div class="news-date">8 Feb, 2012</div>
      <p>Lorem ipsum dolor sit amet, consectetur adipiscing elit. Morbi congue quam vitae lacus vestibulum auctor.</p>
      <a class="news-more">read more...</a>
    </article>
    <article class="news-item">
      <div class="news-date">8 Feb, 2012</div>
      <p>Lorem ipsum dolor sit amet, consectetur adipiscing elit. Morbi congue quam vitae lacus vestibulum auctor.</p>
      <a class="news-more">read more...</a>
    </article>
  </aside>

  <footer class="site-footer">
    <nav class="footer-nav">Home | Company | Services | Careers | Contact Us</nav>
    <div class="footer-legal">Copyright © 2012 Norvane Group.<br>Terms &amp; Condition | Privacy Policy</div>
  </footer>
</body>
</html>
```